Skill Up Salary Up

Full Page
7.5 w x 10 h / 8 w x 10.75 h + .25" bleed
Full-Page Career Course Ad
Project Overview
• Goal: Create a visually attractive, modern, and uncluttered full-page magazine advertisement to list available career courses.
• Tone: Creative, professional, and attention-grabbing to prevent the reader from turning the page. The final design must prioritize readability.

Content Requirements
1. Header/Headline: Must be the primary focus. And grab peoples attention
2. Course Listing: A clear, well-organized list of the career courses.
________________________________________
Design & Aesthetic Directives
1. Layout & Readability (Crucial)
• The final ad must not look crowded or busy.
• Prioritize white space to make the text "breathe" and ensure the course list is easy to scan and read.
• Use a modern, clean, and professional typeface (font choice is critical for the aesthetic).
2. Visual Style
• Aim for a creative, modern, and fresh look. Avoid outdated or generic stock imagery/layouts.
3. Imagery/Graphic Element (Artist's Choice)
You have creative freedom regarding the main graphic element.
• Option A (Photography): Use a photo of a white male American with a collared shirt. The imagery should convey success, focus, or professional development.
• Option B (Vector/Illustration): Use a modern vector graphic, illustration, or abstract design. This could be used to symbolize growth, connection, or a career path.
The choice of graphic element is yours, but it must support the overall modern and uncrowded aesthetic.

Requirements
Must have
• Partial listing .. is part of the Harbor Lantern Course

```html
<!DOCTYPE html>
<html lang="en">
<head>
<meta charset="utf-8">
<title>Skill Up, Salary Up</title>
<link href="https://fonts.googleapis.com/css2?family=Barlow+Semi+Condensed:wght@600;700;800&family=Barlow:wght@400;500;600&display=swap" rel="stylesheet">
<style>
  :root{
    --navy:#14304d;
    --slate:#3d4654;
    --ink:#1f3147;
    --text:#2e3a4a;
    --panel:#f8f8f8;
    --card:#ffffff;
    --page:#ffffff;
  }
  *{margin:0;padding:0;box-sizing:border-box}
  html,body{width:849px;height:1200px;overflow:hidden;background:var(--page)}
  .ad{position:relative;width:849px;height:1200px;background:var(--page);font-family:"Barlow",sans-serif;color:var(--text)}
  .panel{position:absolute;left:81px;top:83px;width:700px;height:1051px;background:var(--panel)}
  .headline{position:absolute;left:0;width:858px;top:111px;text-align:center;font-family:"Barlow Semi Condensed",sans-serif;font-weight:800;font-size:66px;letter-spacing:0.3px;color:var(--navy);line-height:1}
  .subhead{position:absolute;left:0;width:855px;top:195px;text-align:center;font-family:"Barlow Semi Condensed",sans-serif;font-weight:700;font-size:38px;letter-spacing:1.2px;color:var(--slate);line-height:1}
  .tagline{position:absolute;left:0;width:840px;text-align:center;font-family:"Barlow Semi Condensed",sans-serif;font-weight:600;font-size:26px;letter-spacing:1.1px;color:var(--slate);line-height:1}
  .tagline.one{top:245px}
  .tagline.two{top:277px}
  .card{position:absolute;left:126px;top:328px;width:613px;height:789px;background:var(--card)}
  .band{position:absolute;left:126px;background:var(--navy);color:#fff;font-family:"Barlow Semi Condensed",sans-serif;font-weight:700;font-size:29px;line-height:31px;padding:10px 0 0 20px;border-radius:0 5px 0 0}
  .band.enrich{top:328px;width:613px;height:53px}
  .band.books{top:584px;width:381px;height:52px}
  .band.office{top:862px;width:416px;height:81px;padding-top:12px}
  .lead{position:absolute;left:146px;font-family:"Barlow Semi Condensed",sans-serif;font-weight:700;font-size:20px;color:var(--ink);line-height:27px}
  .bullets{position:absolute;left:146px;list-style:none;font-size:19.5px;line-height:30px;color:var(--text)}
  .bullets li::before,.topics li::before{content:"•";display:inline-block;width:20px;font-size:15px;color:var(--ink)}
  .when{position:absolute;left:146px;display:flex;align-items:center;gap:10px;font-family:"Barlow Semi Condensed",sans-serif;font-weight:700;font-size:21px;color:var(--ink)}
  .when svg{width:21px;height:21px}
  .apps{position:absolute;left:146px;top:994px;font-size:19.5px;color:var(--text);white-space:nowrap}
  .apps span{margin-right:14px}
  .apps span::before{content:"• ";color:var(--ink)}
  .topics-title{position:absolute;left:541px;top:419px;font-family:"Barlow Semi Condensed",sans-serif;font-weight:700;font-size:20.5px;color:var(--ink)}
  .topics{position:absolute;left:541px;top:454px;list-style:none;font-size:19.5px;line-height:30.1px;color:var(--text)}
  .topics li{padding-left:19px;text-indent:-19px;max-width:200px}
  .topics li::before{width:19px;text-indent:0}
</style>
</head>
<body>
<div class="ad">
  <div class="panel"></div>
  <h1 class="headline">SKILL UP, SALARY UP</h1>
  <h2 class="subhead">UPCOMING KDL COURSES</h2>
  <p class="tagline one">FOR MEN &amp; WOMEN&nbsp;&nbsp;|&nbsp;&nbsp;IN-PERSON &amp; REMOTE</p>
  <p class="tagline two">PARTIAL SCHOLARSHIPS AVAILABLE</p>

  <div class="card"></div>

  <div class="band enrich">Harbor Lantern</div>
  <p class="lead" style="top:397px">Gain Business Skills &amp; Knowledge to:</p>
  <ul class="bullets" style="top:430px">
    <li>Impress Your Interviewer</li>
    <li>Maximize Income</li>
    <li>Start / Run Your Own Business</li>
  </ul>
  <div class="when" style="top:535px">
    <svg viewBox="0 0 20 20" aria-hidden="true"><rect x="2" y="3.5" width="16" height="14.5" rx="1.5" fill="none" stroke="#14304d" stroke-width="2"/><rect x="2" y="3.5" width="16" height="4" fill="#14304d"/><rect x="5.5" y="1" width="2" height="4" fill="#14304d"/><rect x="12.5" y="1" width="2" height="4" fill="#14304d"/><g fill="#14304d"><rect x="5" y="10" width="2" height="2"/><rect x="9" y="10" width="2" height="2"/><rect x="13" y="10" width="2" height="2"/><rect x="5" y="13.5" width="2" height="2"/><rect x="9" y="13.5" width="2" height="2"/><rect x="13" y="13.5" width="2" height="2"/></g></svg>
    <span>4-5 Months&nbsp;&nbsp;|&nbsp;&nbsp;Starts Nov 2025</span>
  </div>

  <div class="band books">Bookkeeping &amp; Ferncount</div>
  <p class="lead" style="top:650px">Train for a Quality Job or Manage<br>Your Books</p>
  <ul class="bullets" style="top:710px">
    <li>Finance Management</li>
    <li>Customer &amp; Vendor Management</li>
    <li>Advanced Tools</li>
  </ul>
  <div class="when" style="top:816px">
    <svg viewBox="0 0 20 20" aria-hidden="true"><rect x="2" y="3.5" width="16" height="14.5" rx="1.5" fill="none" stroke="#14304d" stroke-width="2"/><rect x="2" y="3.5" width="16" height="4" fill="#14304d"/><rect x="5.5" y="1" width="2" height="4" fill="#14304d"/><rect x="12.5" y="1" width="2" height="4" fill="#14304d"/><g fill="#14304d"><rect x="5" y="10" width="2" height="2"/><rect x="9" y="10" width="2" height="2"/><rect x="13" y="10" width="2" height="2"/><rect x="5" y="13.5" width="2" height="2"/><rect x="9" y="13.5" width="2" height="2"/><rect x="13" y="13.5" width="2" height="2"/></g></svg>
    <span>5 Weeks&nbsp;&nbsp;|&nbsp;&nbsp;Starts Nov 2025</span>
  </div>

  <div class="band office">Office Suite &amp; Computer<br>Basics</div>
  <p class="lead" style="top:957px">The New Job Prerequisite</p>
  <p class="apps"><span>Spreadsheets</span><span>Documents</span><span>Email</span><span>Slides</span></p>
  <div class="when" style="top:1038px">
    <svg viewBox="0 0 20 20" aria-hidden="true"><rect x="2" y="3.5" width="16" height="14.5" rx="1.5" fill="none" stroke="#14304d" stroke-width="2"/><rect x="2" y="3.5" width="16" height="4" fill="#14304d"/><rect x="5.5" y="1" width="2" height="4" fill="#14304d"/><rect x="12.5" y="1" width="2" height="4" fill="#14304d"/><g fill="#14304d"><rect x="5" y="10" width="2" height="2"/><rect x="9" y="10" width="2" height="2"/><rect x="13" y="10" width="2" height="2"/><rect x="5" y="13.5" width="2" height="2"/><rect x="9" y="13.5" width="2" height="2"/><rect x="13" y="13.5" width="2" height="2"/></g></svg>
    <span>7 Months&nbsp;|&nbsp;Starts Dec 2025</span>
  </div>
  <ul class="bullets" style="top:1072px">
    <li>Computer Lab Available for Practice</li>
  </ul>

  <p class="topics-title">Topics Include:</p>
  <ul class="topics">
    <li>Computers</li>
    <li>Marketing</li>
    <li>Sales</li>
    <li>Finance</li>
    <li>Healthcare</li>
    <li>Business Strategy</li>
    <li>Communication</li>
    <li>Ferncount</li>
    <li>Investments</li>
    <li>Real Estate</li>
    <li>Accounting</li>
    <li>Software</li>
    <li>Web &amp; App Development</li>
  </ul>
</div>
</body>
</html>
```